Cardiology practice business card

We need a business card for our cardiology practice "Bellmoor Cardiology". We have a new logo, attached below. We like the colours in the logo - red and charcoal. The front of the business card will need to have the doctors name, address, phone number and email. The back will need to have space to write 2 appointment dates and times.

```html
<!DOCTYPE html>
<html lang="en">
<head>
<meta charset="UTF-8">
<title>Bellmoor Cardiology – Business Card</title>
<link rel="stylesheet" href="https://fonts.googleapis.com/css2?family=Roboto:wght@300;400;700&display=swap">
<style>
  :root {
    --stage: #747f85;
    --card: #ffffff;
    --red: #e52d27;
    --red-label: #d7352b;
    --charcoal: #555555;
    --rule: #c6c6c6;
  }
  * { margin: 0; padding: 0; box-sizing: border-box; }
  html, body { width: 1200px; height: 1000px; overflow: hidden; }
  body {
    background: var(--stage);
    font-family: "Roboto", Arial, sans-serif;
    position: relative;
  }
  .card {
    position: absolute;
    left: 293px;
    width: 615px;
    height: 353px;
    background: var(--card);
    border-radius: 16px;
    overflow: hidden;
  }
  .card--back { top: 72px; }
  .card--front { top: 499px; height: 354px; }

  .brand {
    position: absolute;
    display: flex;
    align-items: center;
    gap: 10px;
    color: var(--red);
    font-weight: 700;
    white-space: nowrap;
  }
  .brand__dot {
    border-radius: 50%;
    background: var(--red);
    flex: none;
  }
  .card--back .brand { left: 45px; top: 152px; font-size: 26px; }
  .card--back .brand__dot { width: 22px; height: 22px; }
  .card--front .brand { left: 0; width: 305px; justify-content: center; top: 78px; font-size: 20px; }
  .card--front .brand__dot { width: 16px; height: 16px; }

  .appointments {
    position: absolute;
    left: 337px;
    top: 84px;
    width: 217px;
  }
  .field {
    position: absolute;
    right: 0;
    display: flex;
    align-items: flex-end;
  }
  .field__label {
    color: var(--red-label);
    font-weight: 700;
    font-size: 16px;
    line-height: 1;
    margin-right: 4px;
  }
  .field--time .field__label { font-size: 17px; }
  .field__line {
    width: 163px;
    height: 2px;
    background: var(--rule);
    margin-bottom: 1px;
  }
  .appointments__divider {
    position: absolute;
    left: 0;
    width: 217px;
    height: 2px;
    background: var(--rule);
    top: 86px;
  }

  .band {
    position: absolute;
    left: 0; right: 0; bottom: 0;
    height: 50px;
    background: var(--red);
    color: #fff;
    font-weight: 700;
    font-size: 23px;
    letter-spacing: 0.5px;
    display: flex;
    align-items: center;
    justify-content: center;
  }

  .contact {
    position: absolute;
    left: 0;
    width: 305px;
    top: 158px;
    text-align: center;
  }
  .contact__name {
    font-size: 19px;
    font-weight: 700;
    color: var(--charcoal);
    letter-spacing: 0.3px;
  }
  .contact__name .first { color: var(--red); }
  .contact__icons {
    display: flex;
    justify-content: center;
    gap: 4px;
    margin-top: 11px;
  }
  .icon {
    width: 26px; height: 26px;
    border-radius: 50%;
    background: var(--red);
    display: flex;
    align-items: center;
    justify-content: center;
  }
  .contact__details {
    margin-top: 9px;
    font-size: 20px;
    font-weight: 300;
    color: var(--charcoal);
    line-height: 24px;
  }
</style>
</head>
<body>

<section class="card card--back">
  <div class="brand"><span class="brand__dot"></span>Bellmoor Cardiology</div>

  <div class="appointments">
    <div class="field field--date" style="top:0;"><span class="field__label">DATE:</span><span class="field__line"></span></div>
    <div class="field field--time" style="top:36px;"><span class="field__label">TIME:</span><span class="field__line"></span></div>
    <div class="appointments__divider"></div>
    <div class="field field--date" style="top:104px;"><span class="field__label">DATE:</span><span class="field__line"></span></div>
    <div class="field field--time" style="top:140px;"><span class="field__label">TIME:</span><span class="field__line"></span></div>
  </div>

  <div class="band">YOUR NEXT APPOINTMENT</div>
</section>

<section class="card card--front">
  <div class="brand"><span class="brand__dot"></span>Bellmoor Cardiology</div>

  <div class="contact">
    <p class="contact__name"><span class="first">NAME</span> SURNAME</p>
    <div class="contact__icons">
      <span class="icon" aria-label="Phone">
        <svg width="14" height="14" viewBox="0 0 24 24"><path fill="#fff" d="M6.6 10.8a15.1 15.1 0 0 0 6.6 6.6l2.2-2.2a1 1 0 0 1 1-.25 11.4 11.4 0 0 0 3.6.57 1 1 0 0 1 1 1V20a1 1 0 0 1-1 1A17 17 0 0 1 3 4a1 1 0 0 1 1-1h3.5a1 1 0 0 1 1 1c0 1.25.2 2.45.57 3.57a1 1 0 0 1-.25 1z"/></svg>
      </span>
      <span class="icon" aria-label="Email">
        <svg width="14" height="14" viewBox="0 0 24 24"><rect x="3" y="6" width="18" height="12" fill="none" stroke="#fff" stroke-width="2"/><path d="M3 6l9 7 9-7" fill="none" stroke="#fff" stroke-width="2"/></svg>
      </span>
      <span class="icon" aria-label="Address">
        <svg width="14" height="14" viewBox="0 0 24 24"><path fill="#fff" d="M12 2a7 7 0 0 0-7 7c0 5 7 13 7 13s7-8 7-13a7 7 0 0 0-7-7zm0 9.5A2.5 2.5 0 1 1 12 6.5a2.5 2.5 0 0 1 0 5z"/></svg>
      </span>
    </div>
    <p class="contact__details">(012) 345-6789<br>name@website.com<br>address</p>
  </div>
</section>

</body>
</html>
```